Business Card design for an International Import Export House

We need a Business Card design for our import export business. We trade in Minerals, Metals, Rice, Sugar, Steel etc.. The design should be minimalistic. It may or may not contain the physical address. In case you want to include the physical address - 418 Verandah Heights, Marlow Sector 9, Gurgaon, Haryana, India, 122009.

Target Market(s)

Steel Mills or Steel Plants, Factories, Mining businesses, Industrial houses, Government Agencies

Industry/Entity Type

Importer

Contact Information for Business Card

Business Name - Kavren Overseas

Font styles to use
Other font styles liked:
• montserrat

Requirements
Must have
• Ravi Kandola - President
• www.kavrenoverseas.com
• ravi@kavrenoverseas.com
• +91-987-654-3217
Nice to have
• worldwide suppliers of ores

```html
<!DOCTYPE html>
<html lang="en">
<head>
<meta charset="utf-8">
<title>Kavren Overseas – Business Card</title>
<link rel="stylesheet" href="https://fonts.googleapis.com/css2?family=Montserrat:wght@700&family=Open+Sans:wght@400;600&display=swap">
<style>
  :root {
    --stage: #8a8a8a;
    --paper: #ffffff;
    --ink: #2b2b2b;
    --teal: #3f8fab;
    --charcoal: #2a2b2d;
    --charcoal-soft: #37393c;
    --light: #f2f2f2;
  }
  * { margin: 0; padding: 0; box-sizing: border-box; }
  html, body { width: 1200px; height: 900px; overflow: hidden; }
  body {
    position: relative;
    background: var(--stage);
    font-family: "Open Sans", Arial, sans-serif;
  }
  .card {
    position: absolute;
    top: 170px;
    width: 347px;
    height: 561px;
    text-align: center;
    overflow: hidden;
  }
  .card--front { left: 259px; background: var(--paper); color: var(--ink); }
  .card--back { left: 631px; background: var(--charcoal); color: var(--light); }

  .tab {
    position: absolute;
    left: 102px;
    width: 143px;
    background: var(--teal);
  }
  .tab--top { top: 0; height: 30px; }
  .tab--bottom { bottom: 0; height: 28px; }

  .brand-dot {
    position: absolute;
    left: 50%;
    border-radius: 50%;
    background: var(--teal);
    transform: translateX(-50%);
  }
  .card--front .brand-dot { top: 100px; width: 92px; height: 92px; }
  .card--back .brand-dot { top: 190px; width: 110px; height: 110px; }

  .brand-name {
    position: absolute;
    left: 0; right: 0;
    font-family: "Montserrat", Arial, sans-serif;
    font-weight: 700;
    letter-spacing: -0.5px;
    white-space: nowrap;
  }
  .card--front .brand-name { top: 249px; font-size: 24px; color: var(--teal); }
  .card--back .brand-name { top: 372px; font-size: 29px; color: var(--light); }

  .person { position: absolute; top: 320px; left: 0; right: 0; }
  .person__name { font-size: 19px; font-weight: 600; color: var(--teal); line-height: 24px; }
  .person__role { font-size: 14.5px; line-height: 20px; }

  .contact-icons {
    position: absolute; top: 380px; left: 0; right: 0;
    display: flex; justify-content: center; gap: 6px;
  }
  .contact-icons svg { width: 10px; height: 10px; fill: var(--teal); }

  .contact {
    position: absolute; top: 394px; left: 0; right: 0;
    list-style: none; font-size: 15px; line-height: 20px;
  }
  .address {
    position: absolute; top: 470px; left: 0; right: 0;
    font-style: normal; font-size: 14.5px; line-height: 20px;
  }

  .world-map {
    position: absolute; left: 12px; top: 20px; width: 322px; height: 520px;
    background: radial-gradient(ellipse at 40% 45%, var(--charcoal-soft) 0%, var(--charcoal) 70%);
  }
  .tagline {
    position: absolute; top: 490px; left: 0; right: 0;
    font-size: 19px; letter-spacing: 0.8px; color: var(--light);
  }
</style>
</head>
<body>
  <section class="card card--front" aria-label="Business card front">
    <div class="tab tab--top"></div>
    <div class="brand-dot"></div>
    <div class="brand-name">KAVREN OVERSEAS</div>
    <div class="person">
      <p class="person__name">Ravi Kandola</p>
      <p class="person__role">President</p>
    </div>
    <div class="contact-icons" aria-hidden="true">
      <svg viewBox="0 0 10 10"><path d="M1 3c0-1 1-2 4-2s4 1 4 2v1H7V3H3v1H1zM2 5h6l1 4H1z"/></svg>
      <svg viewBox="0 0 10 10"><path d="M0 2h10v6H0zM1 3v.4l4 2.6 4-2.6V3L5 5.6z"/></svg>
      <svg viewBox="0 0 10 10"><circle cx="5" cy="5" r="4.5"/></svg>
    </div>
    <ul class="contact">
      <li>+91-987-654-3217</li>
      <li>ravi@kavrenoverseas.com</li>
      <li>www.kavrenoverseas.com</li>
    </ul>
    <address class="address">418 Verandah Heights, Marlow Sector 9,<br>Gurgaon, Haryana, India, 122009.</address>
    <div class="tab tab--bottom"></div>
  </section>

  <section class="card card--back" aria-label="Business card back">
    <div class="world-map" role="img" aria-label="Faint dotted world map background"></div>
    <div class="brand-dot"></div>
    <div class="brand-name">KAVREN OVERSEAS</div>
    <p class="tagline">Worldwide suppliers of Ores</p>
  </section>
</body>
</html>
```